Business Card Design Project

Use our current logo. Clean design.

Industry/Entity Type

Business

Requirements
Must have
• Marisela DUBRANCQ
M. Law
Managing Partner

Alpenvorsa AG
Kornhalmweg 214
CH-3097 Liebefeld

M. +41 79 412 56 27
T. +41 31 928 44 10
F. +41 31 928 44 19

m.dubrancq@alpenvorsa-example.com
www.alpenvorsa-example.com

```html
<!DOCTYPE html>
<html lang="de">
<head>
<meta charset="utf-8">
<title>Alpenvorsa AG – Visitenkarte</title>
<link href="https://fonts.googleapis.com/css2?family=Arimo:wght@400;700&display=swap" rel="stylesheet">
<style>
  :root {
    --canvas: #dcdcdc;
    --card-back: #7b7b7b;
    --card-front: #e6e6e6;
    --accent-bar: #d2d2d2;
    --ink: #1f1f1f;
    --ink-strong: #111111;
    --paper-white: #ffffff;
  }
  * { box-sizing: border-box; margin: 0; padding: 0; }
  html, body {
    width: 1200px; height: 900px; overflow: hidden;
    background: var(--canvas);
    font-family: "Arimo", Arial, sans-serif;
  }
  .stage {
    width: 1200px; height: 900px;
    display: flex; flex-direction: column;
    align-items: center; justify-content: center; gap: 50px;
  }
  .card {
    width: 660px; height: 367px; position: relative; overflow: hidden;
  }
  .card--back {
    background: var(--card-back);
    display: flex; align-items: center; justify-content: center;
  }
  .brand-mark {
    font-size: 44px; font-weight: 400; color: var(--ink-strong);
    letter-spacing: 0.02em;
  }
  .card--front { background: var(--card-front); }
  .accent-bar {
    position: absolute; left: 22px; top: 112px;
    width: 12px; height: 232px; background: var(--accent-bar);
  }
  .brand-watermark {
    position: absolute; right: 34px; top: 130px;
    font-size: 60px; font-weight: 400; color: var(--paper-white);
    letter-spacing: 0.01em; line-height: 1;
  }
  .contact {
    position: absolute; left: 58px; top: 58px;
    font-size: 14px; line-height: 17px; color: var(--ink);
  }
  .contact p + p { margin-top: 0; }
  .contact .group + .group { margin-top: 12px; }
  .contact .label { display: inline-block; width: 16px; font-weight: 700; }
  .contact .name { font-weight: 700; font-size: 15px; color: var(--ink-strong); }
</style>
</head>
<body>
<main class="stage">
  <section class="card card--back" aria-label="Kartenrückseite">
    <span class="brand-mark">Alpenvorsa</span>
  </section>

  <section class="card card--front" aria-label="Kartenvorderseite">
    <div class="accent-bar"></div>
    <span class="brand-watermark" aria-hidden="true">Alpenvorsa</span>
    <div class="contact">
      <div class="group">
        <p>Alpenvorsa AG</p>
        <p>Kornhalmweg 214</p>
        <p>CH-3097 Liebefeld</p>
      </div>
      <div class="group">
        <p><span class="label">M</span>+41 79 412 56 27</p>
        <p><span class="label">T</span>+41 31 928 44 10</p>
        <p><span class="label">F</span>+41 31 928 44 19</p>
      </div>
      <div class="group">
        <p>m.dubrancq@alpenvorsa-example.com</p>
        <p>www.alpenvorsa-example.com</p>
      </div>
      <div class="group">
        <p class="name">Marisela DUBRANCQ</p>
        <p>M. Law</p>
        <p>Managing Partner</p>
      </div>
    </div>
  </section>
</main>
</body>
</html>
```